Dr. Pelham Billboard Sign Design

Family Dental Practice looking for a billboard sign design. We have Attached a Image of Dr Pelham and Her horse she would like to incorporate. The size of the sign is 118" tall and 196" Wide. We hired a previous designer to work on this also but would like to see what other come up with before we decide on a final. Please use something similar for a animal shelter icon to go beside the Animal Shelter Discount statement. You can use the text from the postcard file attached. I know text adjustments will be needed, but more interested in a eye catching design. Themes: Fall/Winter/Mountains/Nature , colors: open but Dr P like purple. We are open to ideas and will answer any questions.
TEXT
Theme: Fall/Winter/Mountain
Image: Dr Pelham with Horse (Same from mailer design)
Text to Keep that needs to be bold and Priority
1. Dr. Rosalind Pelham Family Dentistry
417 Birch Lane Spruce Pine, NC 28704
828-555-3418 | RPelhamDDS@mailvexo.net
(FaceBook icon) RosalindPelhamDDS
2. ACCEPTING NEW PATIENTS
3. Affordable Dentistry for Your Whole Family
4. WE FILE YOUR INSURANCE CLAIMS
5. Discounts for Senior Citizens, Law Enforcement, First Responders, Military Personnel, State Employees and College Students
6. (Cool Animal Shelter Icon) WE OFFER A DISCOUNT TO PATIENTS WHO SUPPORT OUR LOCAL ANIMAL SHELTERS BY ADOPTING, DONATING OR VOLUNTEERING
7. Schedule Your Appointment TODAY!
Target Market(s)
Local Community to Bring in Patients to dental office
Industry/Entity Type
Dental
Look and feel

```html
<!DOCTYPE html>
<html lang="en">
<head>
<meta charset="utf-8">
<title>Dr. Rosalind Pelham Family Dentistry – Billboard</title>
<link href="https://fonts.googleapis.com/css2?family=Open+Sans:wght@400;500;600;700&family=Roboto+Condensed:wght@500&display=swap" rel="stylesheet">
<style>
  :root {
    --cream: #fdf3dc;
    --cream-deep: #f8e6bf;
    --brand-blue: #1e73be;
    --deep-blue: #1f6fb8;
    --sky-blue: #29a3dc;
    --ink: #111111;
    --white: #ffffff;
    --call-yellow: #f4e526;
    --offer-orange: #f05a28;
    --offer-amber: #f7a934;
    --leaf-orange: #f08a1c;
    --leaf-red: #d5421b;
  }
  * { margin: 0; padding: 0; box-sizing: border-box; }
  html, body { width: 1200px; height: 723px; overflow: hidden; background: var(--cream); }
  .billboard {
    position: relative; width: 1200px; height: 723px; overflow: hidden;
    background: radial-gradient(ellipse at 40% 40%, var(--cream) 0%, var(--cream-deep) 100%);
    font-family: "Open Sans", Arial, sans-serif; color: var(--ink);
  }
  .leaves-top-left {
    position: absolute; left: 0; top: 0; width: 146px; height: 137px;
    background: radial-gradient(circle at 20% 20%, var(--leaf-red) 0%, var(--leaf-orange) 55%, rgba(240,138,28,0) 100%);
  }
  .leaves-right {
    position: absolute; right: 0; top: 0; width: 230px; height: 600px;
    background: linear-gradient(160deg, var(--leaf-orange) 0%, var(--leaf-red) 45%, var(--leaf-orange) 75%, rgba(240,138,28,0) 100%);
  }
  .headline-band {
    position: absolute; left: 141px; top: 13px; width: 880px; height: 83px;
    background: rgba(255,255,255,0.9); border-radius: 0 0 30px 30px;
    display: flex; align-items: center; justify-content: center;
  }
  .headline {
    color: var(--brand-blue); font-weight: 600; font-size: 41.5px; letter-spacing: -0.3px; white-space: nowrap;
  }
  .portrait {
    position: absolute; left: 703px; top: 99px; width: 463px; height: 514px;
    background: linear-gradient(180deg, #5a3a28 0%, #3d2a20 45%, #6f7a62 80%, #c9a9b8 100%);
    clip-path: polygon(60px 0, 100% 0, 100% 100%, 0 100%, 0 300px, 60px 200px);
  }
  .perks { position: absolute; left: 36px; top: 156px; list-style: none; }
  .perk {
    position: relative; padding-left: 22px; font-weight: 700; font-size: 21.4px; line-height: 30px; margin-bottom: 14px;
    white-space: nowrap;
  }
  .perk svg { position: absolute; left: 0; top: 8px; }
  .offer {
    position: absolute; left: 36px; top: 392px; width: 633px; height: 78px;
  }
  .offer svg.offer-shape { position: absolute; inset: 0; }
  .offer-icon { position: absolute; left: 8px; top: 14px; }
  .offer-text {
    position: absolute; left: 95px; top: 9px; color: var(--white); font-size: 20.5px; line-height: 30px; white-space: nowrap;
  }
  .cta {
    position: absolute; left: 34px; top: 474px; font-weight: 700; font-size: 35px; line-height: 50px; white-space: nowrap;
  }
  .footer-band { position: absolute; left: 0; top: 0; }
  .call-now { position: absolute; left: 34px; top: 530px; color: var(--call-yellow); font-size: 38px; line-height: 50px; }
  .phone { position: absolute; left: 32px; top: 568px; color: var(--white); font-weight: 500; font-size: 69px; line-height: 84px; letter-spacing: -0.5px; white-space: nowrap; }
  .contact {
    position: absolute; left: 36px; top: 653px; display: flex; align-items: center; gap: 8px;
    color: var(--call-yellow); font-size: 17px; white-space: nowrap;
  }
  .divider { width: 3px; height: 26px; background: var(--white); margin: 0 4px; }
  .social-dot { width: 22px; height: 22px; border-radius: 50%; background: var(--white); }
  .practice {
    position: absolute; left: 560px; top: 616px; width: 628px; text-align: center; white-space: nowrap;
  }
  .practice-name { font-family: "Roboto Condensed", "Arial Narrow", sans-serif; font-weight: 500; font-size: 37px; color: var(--white); line-height: 44px; }
  .practice-address { font-size: 30px; color: var(--ink); line-height: 40px; }
</style>
</head>
<body>
<div class="billboard">
  <div class="leaves-top-left" role="img" aria-label="Autumn maple leaves in orange and red"></div>
  <div class="leaves-right" role="img" aria-label="Cluster of autumn leaves in orange, red and gold"></div>

  <div class="headline-band"><h1 class="headline">Affordable Dentistry for Your Whole Family</h1></div>

  <div class="portrait" role="img" aria-label="Photo of Dr. Pelham standing beside her brown horse with a white blaze"></div>

  <ul class="perks">
    <li class="perk"><svg width="16" height="16" viewBox="0 0 16 16"><path d="M1 1 L8 8 L1 15 M7 1 L14 8 L7 15" stroke="#1e73be" stroke-width="3" fill="none"/></svg>ACCEPTING NEW PATIENTS</li>
    <li class="perk"><svg width="16" height="16" viewBox="0 0 16 16"><path d="M1 1 L8 8 L1 15 M7 1 L14 8 L7 15" stroke="#1e73be" stroke-width="3" fill="none"/></svg>Discounts for Senior Citizens, Law Enforcement, First Responders,<br>Military Personnel, State Employees and College Students</li>
    <li class="perk"><svg width="16" height="16" viewBox="0 0 16 16"><path d="M1 1 L8 8 L1 15 M7 1 L14 8 L7 15" stroke="#1e73be" stroke-width="3" fill="none"/></svg>Refer Friends &amp; Family to Us and Receive a FREE Vantix Gift<br>Card through our referral Program</li>
    <li class="perk"><svg width="16" height="16" viewBox="0 0 16 16"><path d="M1 1 L8 8 L1 15 M7 1 L14 8 L7 15" stroke="#1e73be" stroke-width="3" fill="none"/></svg>WE FILE YOUR INSURANCE CLAIMS</li>
  </ul>

  <div class="offer">
    <svg class="offer-shape" width="633" height="78" viewBox="0 0 633 78">
      <path d="M6 0 H82 L104 78 H6 A6 6 0 0 1 0 72 V6 A6 6 0 0 1 6 0 Z" fill="var(--offer-amber)"/>
      <path d="M82 0 H623 A10 10 0 0 1 633 10 V68 A10 10 0 0 1 623 78 H104 Z" fill="var(--offer-orange)"/>
    </svg>
    <svg class="offer-icon" width="58" height="50" viewBox="0 0 58 50">
      <path d="M29 2 L56 25 H48 V48 H10 V25 H2 Z" fill="var(--brand-blue)" stroke="#fff" stroke-width="2"/>
      <circle cx="29" cy="33" r="8" fill="#fff"/>
    </svg>
    <p class="offer-text">We offer a Discount to Patients who support our local<br>Animal Shelters by Adopting, Donating or Volunteering</p>
  </div>

  <p class="cta">Schedule Your Appointment TODAY!</p>

  <svg class="footer-band" width="1200" height="723" viewBox="0 0 1200 723">
    <rect x="0" y="613" width="1200" height="110" fill="var(--sky-blue)"/>
    <polygon points="0,533 489,533 512,613 489,691 0,691" fill="var(--deep-blue)"/>
  </svg>

  <p class="call-now">Call Now!!</p>
  <p class="phone">828-555-3418</p>
  <div class="contact">
    <span>RPelhamDDS@mailvexo.net</span>
    <span class="divider"></span>
    <span class="social-dot"></span>
    <span>RosalindPelhamDDS</span>
  </div>

  <div class="practice">
    <p class="practice-name">Dr. Rosalind Pelham Family Dentistry</p>
    <p class="practice-address">417 Birch Lane Spruce Pine, NC 28704</p>
  </div>
</div>
</body>
</html>
```